Crestline Slate & Tile Needs a Business Card

Attached you will find your logo, my photo and design guidelines for a new business card. The final design will need two separate files to create an embossed card. The cards will be printed by www.plinkprint.com (Instructions below)
Format is the Zib SQUARE card
Crestline Slate And Tile is a brick and mortar, retail stone and tile shop.
One the front:
Crestline Slate And Tile
Gerald Finchcombe
Owner
48207 Vesper Hollow Blvd
Suite R & T
Charlotte, NC 28953
Cell: 704-555-0183
Web: www.CrestlineSlateAndTile.com
(Make each word of the domain a different or alternating color)
On the back;
Something that shows beautiful colorful tile
Follow the design guide closely please. For more information see this page that describes creating the spot gloss file: https://www.plinkprint.com/us/business-cards/design-guidelines-spot-gloss
The logo is what we would like to have raised spot glossed.
Format is the Zib SQUARE card. See attahced guidlines.

```html
<!DOCTYPE html>
<html lang="en">
<head>
<meta charset="utf-8">
<title>Crestline Slate &amp; Tile — Business Card</title>
<link href="https://fonts.googleapis.com/css2?family=Montserrat:wght@800&family=Sora:wght@400;600&display=swap" rel="stylesheet">
<style>
  :root {
    --page-bg: #e9e9e9;
    --card-white: #ffffff;
    --navy: #233540;
    --gold: #d4922f;
    --rust: #a8482a;
    --rust-edge: #c0622b;
    --sand: #b8a899;
    --sage: #6b7159;
    --text-light: #cfc7bb;
    --text-white: #f3f1ec;
  }
  * { box-sizing: border-box; margin: 0; padding: 0; }
  html, body {
    width: 1200px;
    height: 1200px;
    overflow: hidden;
    background: var(--page-bg);
  }
  .canvas {
    position: relative;
    width: 1200px;
    height: 1200px;
  }
  .card {
    position: absolute;
    left: 204px;
    width: 792px;
    height: 531px;
    background: var(--card-white);
    overflow: hidden;
  }
  .card--front { top: 48px; }
  .card--back { top: 621px; }

  .card__graphic {
    position: absolute;
    inset: 0;
    width: 100%;
    height: 100%;
  }

  .brand-name {
    position: absolute;
    font-family: "Sora", sans-serif;
    font-weight: 600;
    color: var(--navy);
    text-align: center;
    line-height: 1.2;
  }
  .card--front .brand-name {
    left: 40px;
    top: 210px;
    width: 280px;
    font-size: 28px;
  }
  .card--back .brand-name {
    left: 0;
    right: 0;
    top: 240px;
    font-size: 44px;
    letter-spacing: 1px;
  }

  .owner {
    position: absolute;
    right: 48px;
    top: 80px;
    text-align: right;
  }
  .owner__name {
    font-family: "Montserrat", sans-serif;
    font-weight: 800;
    font-size: 33px;
    line-height: 1.02;
    color: var(--gold);
    text-transform: uppercase;
    letter-spacing: 0.3px;
  }
  .owner__title {
    margin-top: 8px;
    font-family: "Sora", sans-serif;
    font-weight: 400;
    font-size: 20px;
    color: var(--text-white);
  }

  .contact {
    position: absolute;
    right: 48px;
    font-family: "Sora", sans-serif;
    font-weight: 400;
    font-size: 21px;
    color: var(--text-light);
    text-align: right;
    line-height: 1.3;
  }
  .contact--details { top: 300px; }
  .contact--web { top: 450px; }
  .contact__row {
    display: flex;
    justify-content: flex-end;
    align-items: center;
  }
  .contact__row--indent { padding-right: 30px; }
  .contact__icon {
    width: 18px;
    height: 18px;
    margin-left: 12px;
    flex: none;
  }
</style>
</head>
<body>
<main class="canvas">

  <section class="card card--front" aria-label="Business card front">
    <svg class="card__graphic" viewBox="0 0 634 425" preserveAspectRatio="none" aria-hidden="true">
      <polygon class="band band--gold" fill="var(--gold)" points="167,0 634,0 634,425 167,425 349.2,182.2"/>
      <polygon class="band band--rust" fill="var(--rust)" points="205,0 634,0 634,425 167,425 364.9,159.9"/>
      <polygon class="band band--sand" fill="var(--sand)" points="245,0 634,0 634,425 167,425 382,137"/>
      <polygon class="band band--rust-edge" fill="var(--rust-edge)" points="268,0 634,0 634,425 167,425 391.8,123.8"/>
      <polygon class="band band--sage" fill="var(--sage)" points="167,425 190,425 372,181 349.2,182.2"/>
      <polygon class="panel panel--navy" fill="var(--navy)" points="277,0 634,0 634,425 190,425 408.8,131.8"/>
    </svg>

    <p class="brand-name">Crestline Slate &amp; Tile</p>

    <div class="owner">
      <h1 class="owner__name">Gerald<br>Finchcombe</h1>
      <p class="owner__title">Owner</p>
    </div>

    <div class="contact contact--details">
      <p class="contact__row">704-555-0183
        <svg class="contact__icon" viewBox="0 0 24 24" aria-hidden="true">
          <path fill="none" stroke="var(--gold)" stroke-width="2" stroke-linecap="round" stroke-linejoin="round" d="M5 3h4l2 5-2.5 1.5a11 11 0 0 0 6 6L16 13l5 2v4a2 2 0 0 1-2 2A16 16 0 0 1 3 5a2 2 0 0 1 2-2z"/>
        </svg>
      </p>
      <p class="contact__row">48207 Vesper Hollow Blvd
        <svg class="contact__icon" viewBox="0 0 24 24" aria-hidden="true">
          <path fill="var(--gold)" d="M12 2a7 7 0 0 0-7 7c0 5 7 13 7 13s7-8 7-13a7 7 0 0 0-7-7zm0 9.5A2.5 2.5 0 1 1 12 6.5a2.5 2.5 0 0 1 0 5z"/>
        </svg>
      </p>
      <p class="contact__row contact__row--indent">Suite R &amp; T</p>
      <p class="contact__row contact__row--indent">Charlotte, NC 28953</p>
    </div>

    <div class="contact contact--web">
      <p class="contact__row">www.CrestlineSlateAndTile.com
        <svg class="contact__icon" viewBox="0 0 24 24" aria-hidden="true">
          <circle cx="12" cy="12" r="9" fill="var(--gold)"/>
          <path fill="none" stroke="var(--navy)" stroke-width="1.4" d="M3 12h18M12 3c3 3 3 15 0 18M12 3c-3 3-3 15 0 18M5 7.5h14M5 16.5h14"/>
        </svg>
      </p>
    </div>
  </section>

  <section class="card card--back" aria-label="Business card back">
    <p class="brand-name">Crestline Slate &amp; Tile</p>
  </section>

</main>
</body>
</html>
```